Construction Contractor
Bayt Nuwaris
Professional
Fahad Omar Qurashi
Owner
Rawda Street P.O.Box 483920 Jeddah 24719 Saudi Arabia
baytnuwaris@mailbox-example.com
We need Logo to be in the middle and company name under the logo

```html
<!DOCTYPE html>
<html lang="en">
<head>
<meta charset="utf-8">
<title>Bayt Nuwaris – Business Card</title>
<link rel="stylesheet" href="https://fonts.googleapis.com/css2?family=Montserrat:wght@500;700&family=Open+Sans:wght@400;600&display=swap">
<style>
  :root {
    --backdrop: #7b7b7b;
    --card: #ffffff;
    --gold: #b8923f;
    --brown: #4e3c2b;
    --ink: #3c3c3c;
    --rule: #b8923f;
  }
  html, body {
    margin: 0;
    width: 1200px;
    height: 908px;
    overflow: hidden;
    background: radial-gradient(ellipse at 40% 30%, #8e8e8e, var(--backdrop));
    font-family: "Open Sans", sans-serif;
  }
  .stage {
    width: 1200px;
    height: 908px;
    display: flex;
    flex-direction: column;
    align-items: center;
    justify-content: center;
    gap: 56px;
  }
  .card {
    width: 600px;
    height: 343px;
    background: var(--card);
    border-radius: 22px;
    box-shadow: 0 14px 30px rgba(0,0,0,.35);
    position: relative;
    box-sizing: border-box;
  }
  .brand {
    display: flex;
    flex-direction: column;
    align-items: center;
    gap: 10px;
  }
  .brand-square {
    width: 34px;
    height: 34px;
    background: var(--gold);
  }
  .brand-name {
    font-family: "Montserrat", sans-serif;
    font-weight: 700;
    color: var(--brown);
    letter-spacing: 1px;
    text-transform: uppercase;
    white-space: nowrap;
  }
  .card-front {
    display: flex;
    align-items: center;
    justify-content: center;
  }
  .card-front .brand-name { font-size: 30px; }
  .card-front .brand-square { width: 58px; height: 58px; }

  .card-back {
    display: grid;
    grid-template-columns: 250px 1px 1fr;
    align-items: center;
    padding: 0 30px;
  }
  .identity {
    display: flex;
    flex-direction: column;
    align-items: center;
    gap: 34px;
  }
  .card-back .brand-name { font-size: 20px; }
  .person {
    text-align: center;
  }
  .person-name {
    font-family: "Montserrat", sans-serif;
    font-weight: 500;
    font-size: 18px;
    color: var(--gold);
    margin: 0;
    white-space: nowrap;
  }
  .person-role {
    font-size: 13px;
    color: var(--ink);
    margin: 4px 0 0;
  }
  .divider {
    width: 1px;
    height: 210px;
    background: var(--rule);
  }
  .contact {
    list-style: none;
    margin: 0;
    padding: 0 0 0 22px;
    font-size: 11.5px;
    line-height: 1.35;
    color: var(--ink);
  }
  .contact li {
    display: flex;
    align-items: flex-start;
    gap: 8px;
    margin-bottom: 5px;
    white-space: nowrap;
  }
  .contact .license { color: var(--gold); margin-bottom: 8px; }
  .contact svg {
    width: 12px;
    height: 12px;
    flex: none;
    margin-top: 2px;
    fill: var(--brown);
  }
</style>
</head>
<body>
<main class="stage">
  <section class="card card-front">
    <div class="brand">
      <span class="brand-square"></span>
      <span class="brand-name">Bayt Nuwaris</span>
    </div>
  </section>

  <section class="card card-back">
    <div class="identity">
      <div class="brand">
        <span class="brand-square"></span>
        <span class="brand-name">Bayt Nuwaris</span>
      </div>
      <div class="person">
        <p class="person-name">Fahad Omar Qurashi</p>
        <p class="person-role">Owner</p>
      </div>
    </div>
    <div class="divider"></div>
    <ul class="contact">
      <li class="license">License No. 4030000000</li>
      <li>
        <svg viewBox="0 0 12 12" aria-hidden="true"><path d="M6 0a4 4 0 0 0-4 4c0 3 4 8 4 8s4-5 4-8a4 4 0 0 0-4-4zm0 5.5A1.5 1.5 0 1 1 6 2.5a1.5 1.5 0 0 1 0 3z"/></svg>
        <span>Rawda Street<br>P.O.Box 483920<br>Jeddah 24719, Saudi Arabia</span>
      </li>
      <li>
        <svg viewBox="0 0 12 12" aria-hidden="true"><path d="M2.5 0.5l2 2.2-1 1.3a7 7 0 0 0 4.5 4.5l1.3-1 2.2 2-1 1.9C5.5 11.4 0.6 6.5 0.6 1.5z"/></svg>
        <span>+966 12 000 1234</span>
      </li>
      <li>
        <svg viewBox="0 0 12 12" aria-hidden="true"><rect x="3" y="0" width="6" height="12" rx="1.2"/><rect x="4" y="1.5" width="4" height="7.5" fill="#fff"/></svg>
        <span>+966 50 000 5678</span>
      </li>
      <li>
        <svg viewBox="0 0 12 12" aria-hidden="true"><rect x="3" y="0" width="6" height="12" rx="1.2"/><rect x="4" y="1.5" width="4" height="7.5" fill="#fff"/></svg>
        <span>+966 55 000 9012</span>
      </li>
      <li>
        <svg viewBox="0 0 12 12" aria-hidden="true"><path d="M0 2h12v8H0z"/><path d="M0.5 2.5L6 7l5.5-4.5" stroke="#fff" stroke-width="1" fill="none"/></svg>
        <span>baytnuwaris@mailbox-example.com</span>
      </li>
    </ul>
  </section>
</main>
</body>
</html>
```